Tech business card design

We need an amazing business card design for our new business 'Brakka' a marketing tech startup based in Sydney, Australia. We provide an online marketplace for businesses to search and buy advertising media, connect with service providers and learn more about marketing. We wish to communicate 'cool tech', reliability and professionalism and design based around our logo.

Target Market(s)

Business Owners

Contact Information for Business Card

Name
Position
Email Address
Website
Phone Number

Font styles to use
Other font styles liked:
• Avenir & Avenir Next

Colors

Designer to choose colors to be used in the design.

```html
<!DOCTYPE html>
<html lang="en">
<head>
<meta charset="utf-8">
<title>Brakka business card</title>
<link rel="stylesheet" href="https://fonts.googleapis.com/css2?family=Mulish:wght@300;400;900&display=swap">
<style>
  :root {
    --bg: #8a8a8c;
    --bg-dark: #4a4a4c;
    --navy: #1f1d33;
    --navy-deep: #16152a;
    --purple-glow: #4a3d66;
    --band: #1c1b2b;
    --paper: #efefef;
    --ink: #1e1d2e;
    --grey-text: #9a9aa3;
    --white: #ffffff;
  }
  * { margin: 0; padding: 0; box-sizing: border-box; }
  html, body { width: 1200px; height: 900px; overflow: hidden; }
  body {
    background: radial-gradient(ellipse at 45% 40%, var(--bg) 0%, var(--bg-dark) 100%);
    font-family: "Mulish", sans-serif;
    position: relative;
  }
  .card {
    position: absolute;
    top: 300px;
    width: 520px;
    height: 300px;
    border-radius: 22px;
    overflow: hidden;
    box-shadow: 0 14px 30px rgba(0,0,0,0.35);
  }
  /* Contact side */
  .card--contact { left: 50px; background: var(--paper); }
  .contact__band {
    position: absolute; left: 0; top: 0; width: 100%; height: 128px;
    background: var(--band);
  }
  .contact__notch {
    position: absolute; top: 128px; width: 0; height: 0;
    border-left: 7px solid transparent; border-right: 7px solid transparent;
    border-top: 8px solid var(--band);
  }
  .contact__notch--left { left: 40px; }
  .contact__notch--right { right: 40px; }
  .contact__name {
    position: absolute; left: 42px; top: 40px;
    color: var(--grey-text); font-weight: 300; font-size: 24px; letter-spacing: 0.5px;
  }
  .contact__role {
    position: absolute; left: 42px; top: 72px;
    color: #6f6f78; font-weight: 400; font-size: 14px;
  }
  .contact__icons {
    position: absolute; left: 42px; top: 158px; width: 26px; height: 74px;
    background: var(--band); border-radius: 3px;
  }
  .contact__icons svg { display: block; margin: 5px auto 0; }
  .contact__list { position: absolute; left: 80px; top: 156px; list-style: none; }
  .contact__list li {
    width: 172px; font-size: 13px; color: #444; padding: 2px 0 3px;
    border-bottom: 1.5px solid #333; margin-bottom: 2px;
    white-space: nowrap;
  }
  .contact__logo {
    position: absolute; right: 48px; bottom: 30px;
    color: var(--ink); font-weight: 900; font-size: 58px; letter-spacing: -1.5px; line-height: 1;
  }
  .contact__logo .wordmark { position: relative; }
  .tm { position: absolute; font-size: 9px; font-weight: 400; letter-spacing: 0; }
  .contact__logo .tm { right: -14px; bottom: 2px; }
  /* Brand side */
  .card--brand {
    left: 630px;
    background:
      radial-gradient(ellipse 70% 45% at 60% 38%, var(--purple-glow) 0%, transparent 100%),
      linear-gradient(180deg, var(--navy) 0%, var(--navy-deep) 100%);
  }
  .brand__arc { position: absolute; inset: 0; }
  .brand__logo {
    position: absolute; left: 0; width: 100%; top: 86px; text-align: center;
    color: var(--white); font-weight: 900; font-size: 96px; letter-spacing: -2px; line-height: 1;
  }
  .brand__logo .wordmark { position: relative; }
  .brand__logo .tm { right: -14px; bottom: 0; color: #d8d8e0; }
  .brand__web {
    position: absolute; left: 0; width: 100%; top: 212px; text-align: center;
    color: #c5c3d3; font-size: 12px; letter-spacing: 4px; font-weight: 400;
  }
</style>
</head>
<body>
  <section class="card card--contact" aria-label="Business card contact side">
    <div class="contact__band"></div>
    <div class="contact__notch contact__notch--left"></div>
    <div class="contact__notch contact__notch--right"></div>
    <p class="contact__name">DANIEL MOSS</p>
    <p class="contact__role">Founder, Director</p>
    <div class="contact__icons">
      <svg width="12" height="16" viewBox="0 0 12 16" aria-hidden="true"><rect x="2" y="1" width="8" height="14" rx="1.5" fill="none" stroke="#ddd" stroke-width="1.4"/></svg>
      <svg width="14" height="12" viewBox="0 0 14 12" aria-hidden="true"><rect x="1" y="2" width="12" height="8" fill="none" stroke="#ddd" stroke-width="1.3"/><path d="M1 2l6 5 6-5" fill="none" stroke="#ddd" stroke-width="1.3"/></svg>
      <svg width="14" height="14" viewBox="0 0 14 14" aria-hidden="true"><circle cx="7" cy="7" r="6" fill="#ddd"/><path d="M1 7h12M7 1c3 3 3 9 0 12M7 1c-3 3-3 9 0 12" fill="none" stroke="#1c1b2b" stroke-width="1"/></svg>
    </div>
    <ul class="contact__list">
      <li>+61(0)400 555 218</li>
      <li>daniel@brakkamedia.com.au</li>
      <li>www.brakkamedia.com.au</li>
    </ul>
    <div class="contact__logo"><span class="wordmark">brakka<span class="tm">TM</span></span></div>
  </section>

  <section class="card card--brand" aria-label="Business card brand side">
    <svg class="brand__arc" width="520" height="300" viewBox="0 0 520 300" aria-hidden="true">
      <path d="M0 30 Q260 -10 520 30" fill="none" stroke="rgba(255,255,255,0.06)" stroke-width="2"/>
      <path d="M0 250 Q260 200 520 250" fill="none" stroke="rgba(255,255,255,0.05)" stroke-width="2"/>
    </svg>
    <div class="brand__logo"><span class="wordmark">brakka<span class="tm">TM</span></span></div>
    <p class="brand__web">www.brakkamedia.com.au</p>
  </section>
</body>
</html>
```